Business Card: RW Office Partners - Your tidy answer finder

Business Name: RW Office Partners
Website: www.rwofficepartners.com.au
Email: marisol@rwofficepartners.com.au
Mobile: 61 487 902 346
Facebook: @rwofficepartners
Instrgram: @rwofficepartners

Brading Colours:
HEX
#986474
#ddccd3
#7a8498
#c9d8e4
#000000
#ffffff

Tag Line: Your organised problem solver

Link to DRAFT website:
https://helpdeskhub.sitebuilderx.com/rw-office-partners

About Page from the website:
My name is Marisol Bramwell, and I would love to assist you to become more productive in your day to day and achieve your business and personal goals.
My mission is to give you time, time to work on the important tasks of your business or to be able to spend more time with your family. I will take on the tasks you don’t have time for, don’t know well or simply don’t like to do.
I have an extensive background in Administration, Tender Coordination, Document Control, WHS and Quality Management working primarily in the Construction, Mining and Corporate World.
I am passionate about being organised, having order and making things in your life (and mine) easier! I love to watch something unfold and grow into something amazing! I am known for being the go-to problem solver, the organiser of all things, producing high standards of work even under pressure. I’m also a confident communicator, and I understand that you’re busy running your business.

Target Market(s)

Small to Medium Business who require assistance in their business by a virtual assistant.

Industry/Entity Type

Virtual Assistant

Contact Information for Business Card

Mobile: 61 487 902 346

Font styles to use
Sans Serif

Colors
ffffff

Requirements
Must have
• Branding Colours as outlined.
Contact Details as outlined.
Logo as provided.
Proper contact details - mobile, facebook, instragm, website.
Simple, Elegant, very clean looking.
Should not have
• Note cute with pictures.
Not too girly as still want to market to construction companies.

```html
<!DOCTYPE html>
<html lang="en">
<head>
<meta charset="utf-8">
<title>RW Office Partners – Business Card</title>
<link href="https://fonts.googleapis.com/css2?family=Arimo:wght@400&family=Cabin:wght@600&display=swap" rel="stylesheet">
<style>
  :root {
    --mauve: #986474;
    --slate: #7a8498;
    --white: #ffffff;
    --backdrop: #cbcbcb;
  }
  html, body {
    margin: 0;
    padding: 0;
    width: 1125px;
    height: 1200px;
    overflow: hidden;
    background: var(--backdrop);
  }
  .canvas {
    position: relative;
    width: 1125px;
    height: 1200px;
  }
  .card {
    position: absolute;
    left: 178px;
    width: 768px;
    height: 437px;
    border-radius: 21px;
    overflow: hidden;
  }
  .card--front { top: 140px; background: var(--white); }
  .card--back  { top: 626px; background: var(--slate); }

  .brand-name {
    position: absolute;
    margin: 0;
    font-family: "Cabin", sans-serif;
    font-weight: 600;
    white-space: nowrap;
    line-height: 1;
  }
  .card--front .brand-name {
    left: 78px;
    top: 179px;
    font-size: 29px;
    color: var(--mauve);
  }
  .card--back .brand-name {
    left: 0;
    width: 768px;
    text-align: center;
    top: 192px;
    font-size: 50px;
    color: var(--white);
  }

  .divider {
    position: absolute;
    left: 384px;
    top: 138px;
    width: 2px;
    height: 159px;
    background: var(--slate);
  }

  .contact {
    position: absolute;
    left: 414px;
    top: 138px;
  }
  .contact__title {
    margin: 0 0 9px;
    font-family: "Cabin", sans-serif;
    font-weight: 600;
    font-size: 27px;
    line-height: 1.1;
    color: var(--mauve);
    white-space: nowrap;
  }
  .contact__list {
    list-style: none;
    margin: 0;
    padding: 0;
  }
  .contact__item {
    display: flex;
    align-items: center;
    height: 23.5px;
    font-family: "Arimo", sans-serif;
    font-size: 18px;
    color: var(--slate);
    white-space: nowrap;
  }
  .contact__icon {
    width: 11px;
    height: 11px;
    margin-right: 8px;
    flex: none;
    fill: var(--mauve);
  }

  .tagline {
    position: absolute;
    left: 0;
    width: 768px;
    top: 380px;
    margin: 0;
    text-align: center;
    font-family: "Arimo", sans-serif;
    font-size: 17px;
    color: var(--white);
  }
</style>
</head>
<body>
<main class="canvas">

  <section class="card card--front" aria-label="Card front">
    <p class="brand-name">RW Office Partners</p>
    <div class="divider"></div>
    <div class="contact">
      <h1 class="contact__title">RW Office Partners</h1>
      <ul class="contact__list">
        <li class="contact__item">
          <svg class="contact__icon" viewBox="0 0 12 12" aria-hidden="true"><path d="M2.5 1 L4.5 1 L5.2 3.6 L3.9 4.6 Q5 7 7.4 8.1 L8.4 6.8 L11 7.5 L11 9.5 Q10.5 11 9 11 Q1 10 1 3 Q1 1.5 2.5 1 Z"/></svg>
          61 487 902 346
        </li>
        <li class="contact__item">
          <svg class="contact__icon" viewBox="0 0 12 12" aria-hidden="true"><path d="M0 2.5 H12 V9.5 H0 Z M0.8 3 L6 7 L11.2 3" stroke="#fff" stroke-width="0.9"/></svg>
          marisol@rwofficepartners.com.au
        </li>
        <li class="contact__item">
          <svg class="contact__icon" viewBox="0 0 12 12" aria-hidden="true"><circle cx="6" cy="6" r="5.5"/><path d="M0.5 6 H11.5 M6 0.5 Q3 6 6 11.5 M6 0.5 Q9 6 6 11.5" stroke="#fff" stroke-width="0.8" fill="none"/></svg>
          www.rwofficepartners.com.au
        </li>
        <li class="contact__item">
          <svg class="contact__icon" viewBox="0 0 12 12" aria-hidden="true"><rect x="0.5" y="0.5" width="11" height="11"/></svg>
          @rwofficepartners
        </li>
        <li class="contact__item">
          <svg class="contact__icon" viewBox="0 0 12 12" aria-hidden="true"><rect x="0.5" y="0.5" width="11" height="11"/></svg>
          @rwofficepartners
        </li>
      </ul>
    </div>
  </section>

  <section class="card card--back" aria-label="Card back">
    <p class="brand-name">RW Office Partners</p>
    <p class="tagline">Your tidy answer finder</p>
  </section>

</main>
</body>
</html>
```